Professional Website for Commercial Real Estate Broker

I own a small boutique commercial real estate company called Birchwell Holdings.
My current website is www.teamdurnio.com and is hosted on hostlark. I am looking for an all new website that will allow me to compete with bigger players in our industry. In other words, I need something professional, sleek, and functional.

I am looking for a designer that can take my complete website all the way to coding, migration, and launch. I understand that this may be an add'l charge, so please include with your design submission what the add'l charge will be to take the website to launch with all functionality as described below.

As an example of a page in my industry that I like please check out: www.marcusolverin.com.

My logo is attached and my main colors are the blue, white, grey - similar to the logo.

I am looking for a five page website with the following pages:

Home
Birchwell Team
Services
Sold Properties
Contact

A couple of features that I will want on the site are:

- I want to make sure that we can imbed a news commercial real estate news feed from: http://www.plazowire.com/news/ on the website's home page, similar to how it is on marcusolverin.com.

- Sold Properties page will allow me to upload the following information on to the website so that I can add new properties that I have recently sold on a weekly or monthly basis. I would like the information to be displayed similarly to http://www.marcusolverin.com/properties.html . I should be able to upload: picture, price, bldg size, lot size, closing date for each property. This will require a user friendly back end that I can navigate.

- On the home page, I also want to have a form where visitors can request a Market Analysis of their property by entering: Name, property address, email address, phone number. I will be sent an email with this information and I can follow up via telephone or email direct.

- The Birchwell Team page will have a picture, contact info, and brief bio for each member of the team. I would like to be able to adjust this on a user friendly back end.

I have included my Company Logo. Feel free to use any text from my current website: www.teamdurnio.com. Also, any sleek looking stock photos of office / commercial buildings can be used for the initial design purposes.

I look forward to getting your design submittal and moving forward asap!

Target Market(s)

Los Angeles real estate brokers, developers, and investors.

Industry/Entity Type

Real Estate

Coding

Coded - Design and coding required

Number of Pages Required

5+ page

Font styles to use
Sans Serif

Colors
ffffff
85abd2
0455a3
b2b2b2
000000
3276b5

Requirements
Must have
• Sleek and professional design.
• - I want to make sure that we can imbed a news commercial real estate news feed from: http://www.plazowire.com/news/ on the website's home page, similar to how it is on marcusolverin.com.
• - Sold Properties page will allow me to upload the following information on to the website so that I can add new properties that I have recently sold on a weekly or monthly basis. I would like the information to be displayed similarly to http://www.marcusolverin.com/properties.html . I should be able to upload: picture, price, bldg size, lot size, closing date for each property. This will require a user friendly back end that I can navigate.
• - On the home page, I also want to have a form where visitors can request a Market Analysis of their property by entering: Name, property address, email address, phone number. I will be sent an email with this information and I can follow up via telephone or email direct.
Nice to have
• Dynamic banner on the home page with beautiful photos that change every few seconds.

```html
<!DOCTYPE html>
<html lang="en">
<head>
<meta charset="utf-8">
<title>Birchwell Holdings — Commercial Real Estate</title>
<link rel="stylesheet" href="https://fonts.googleapis.com/css2?family=Poppins:wght@300;400;500;600&display=swap">
<style>
:root{
  --blue-deep:#0455a3;
  --blue-mid:#3276b5;
  --blue-soft:#85abd2;
  --blue-hero:#1d5aa8;
  --panel:rgba(28,52,92,.88);
  --grey:#b2b2b2;
  --grey-text:#7a7a7a;
  --ink:#000000;
  --white:#ffffff;
  --paper:#f8f8f8;
  --font:'Poppins', sans-serif;
}
*{margin:0;padding:0;box-sizing:border-box}
html,body{width:1200px;height:2773px;overflow:hidden}
body{font-family:var(--font);background:var(--white);color:var(--ink);position:relative}

/* Hero */
.hero{position:absolute;left:0;top:0;width:1200px;height:675px;
  background:linear-gradient(160deg,#2a69b4 0%,#1c58a4 45%,#164b91 100%)}
.hero-photo{position:absolute;inset:0;
  background:
   linear-gradient(100deg,rgba(255,255,255,.08) 0 18%,transparent 18% 22%,rgba(255,255,255,.06) 22% 30%,transparent 30%),
   linear-gradient(75deg,transparent 0 62%,rgba(10,40,90,.25) 62% 72%,transparent 72% 85%,rgba(255,255,255,.05) 85%)}
.brand{position:absolute;left:153px;top:46px;color:var(--white);font-weight:600;font-size:24px;
  display:flex;align-items:center;gap:10px}
.brand-mark{width:16px;height:16px;background:var(--white)}
.main-nav{position:absolute;top:54px;left:479px;display:flex;gap:0}
.main-nav a{position:absolute;color:var(--white);text-decoration:none;font-size:15px;font-weight:500;white-space:nowrap}
.hero-title{position:absolute;left:172px;top:286px;color:var(--white);font-size:38px;font-weight:500}
.hero-sub{position:absolute;left:173px;top:344px;color:#dfe8f4;font-size:15px;font-weight:300}
.btn{position:absolute;width:186px;height:45px;border-radius:5px;background:var(--blue-soft);
  color:var(--white);font-size:14px;font-weight:500;display:flex;align-items:center;justify-content:center}
.hero .btn{left:174px;top:388px;background:rgba(133,171,210,.85)}
.slider-dots{position:absolute;left:173px;top:601px;display:flex;gap:19px}
.slider-dots span{width:9px;height:9px;border-radius:50%;background:var(--white)}
.slider-dots span:first-child{opacity:.55}

/* Market analysis form */
.analysis{position:absolute;left:690px;top:152px;width:333px;height:469px;background:var(--panel);border-radius:6px;padding:26px 22px}
.analysis .eyebrow{color:var(--white);font-size:16px;font-weight:500}
.analysis h2{color:var(--blue-soft);font-size:27px;font-weight:500;line-height:1.1}
.field{position:absolute;left:22px;width:288px;border-bottom:1.5px solid rgba(255,255,255,.8);
  color:var(--white);font-size:10px;font-weight:500;padding-bottom:12px}
.submit{position:absolute;left:24px;top:371px;width:120px;height:36px;background:var(--blue-deep);border-radius:4px;
  color:var(--white);font-size:12px;font-weight:500;display:flex;align-items:center;justify-content:center}
.required{position:absolute;left:26px;top:426px;color:#d6e0ee;font-size:9px}

/* Welcome */
.welcome{position:absolute;left:0;top:675px;width:1200px;height:545px;background:var(--white)}
.welcome-band{position:absolute;left:675px;top:0;width:525px;height:545px;
  background:radial-gradient(circle at 30% 30%,#3a72b5 0,#1c58a4 40%,#16508f 100%)}
.welcome-photo{position:absolute;left:640px;top:139px;width:401px;height:266px;
  background:linear-gradient(135deg,#3f7a2c 0%,#5a8f3a 35%,#8a9aa0 50%,#4f8434 70%,#2f6424 100%);
  box-shadow:0 8px 18px rgba(0,0,0,.35)}
.welcome-kicker{position:absolute;left:161px;top:124px;font-size:15px;font-weight:500}
.welcome-title{position:absolute;left:159px;top:134px;font-size:49px;font-weight:500;letter-spacing:.3px}
.welcome-copy{position:absolute;left:160px;top:220px;width:460px;font-size:14.5px;line-height:24px;color:var(--grey-text);font-weight:300}
.welcome .btn{left:159px;top:405px}

/* News */
.news{position:absolute;left:0;top:1220px;width:1200px;height:1443px;background:var(--paper)}
.news-kicker{position:absolute;left:159px;top:70px;font-size:14px;font-weight:500}
.news-title{position:absolute;left:157px;top:84px;font-size:47px;font-weight:500}
.news-list{position:absolute;left:159px;top:189px;width:880px}
.news-item{height:237px;border-top:1.5px dashed var(--grey);position:relative}
.news-item:last-child{border-bottom:1.5px dashed var(--grey);height:238px}
.news-thumb{position:absolute;left:0;top:43px;width:190px;height:148px}
.news-body{position:absolute;left:211px;top:66px;width:670px}
.news-body h3{color:var(--blue-deep);font-size:14.5px;font-weight:400}
.news-body p{color:var(--grey-text);font-size:11px;line-height:18px;margin-top:9px;font-weight:300}
.news-body time{display:block;margin-top:9px;font-size:9px;font-weight:600}
.scroll-track{position:absolute;left:1076px;top:235px;width:20px;height:1152px;background:var(--white)}
.scroll-thumb{position:absolute;left:4px;top:0;width:9px;height:148px;background:#e3e3e3}

/* Footer */
.site-footer{position:absolute;left:0;top:2663px;width:1200px;height:110px;background:var(--white)}
.foot-nav{position:absolute;left:159px;top:63px;font-size:11px;color:#444}
.foot-brand{position:absolute;left:558px;top:55px;color:var(--blue-deep);font-weight:600;font-size:18px}
.copyright{position:absolute;right:159px;top:63px;font-size:11px;color:#444}
</style>
</head>
<body>

<header class="hero">
  <div class="hero-photo" role="img" aria-label="Upward view of blue-tinted glass office towers"></div>
  <div class="brand"><span class="brand-mark"></span>Birchwell</div>
  <nav class="main-nav">
    <a style="left:0">Home</a>
    <a style="left:87px">Birchwell Team</a>
    <a style="left:234px">Services</a>
    <a style="left:320px">Sold Properties</a>
    <a style="left:473px">Contact</a>
  </nav>
  <h1 class="hero-title">Birchwell Holdings</h1>
  <p class="hero-sub">We are a small boutique commercial real estate company</p>
  <div class="btn">Learn More</div>
  <div class="slider-dots"><span></span><span></span><span></span><span></span></div>

  <form class="analysis">
    <div class="eyebrow">Request a</div>
    <h2>Market Analysis</h2>
    <div class="field" style="top:114px">Name *</div>
    <div class="field" style="top:178px">Property Address</div>
    <div class="field" style="top:240px">E-Mail Address *</div>
    <div class="field" style="top:312px">Phone Number *</div>
    <div class="submit">Submit</div>
    <div class="required">* Required Fields</div>
  </form>
</header>

<section class="welcome">
  <div class="welcome-band" role="img" aria-label="Soft blurred blue texture"></div>
  <div class="welcome-photo" role="img" aria-label="Aerial view of a tree-lined residential intersection"></div>
  <div class="welcome-kicker">Welcome to</div>
  <h2 class="welcome-title">Birchwell Holdings</h2>
  <p class="welcome-copy">Birchwell Holdings is a commercial real estate brokerage firm that provides a range of services to assist each of our clients in reaching their real estate objectives quickly and efficiently. Our focus on Southern California investment properties allows us to have a unique and focused perspective on this highly competitive market.</p>
  <div class="btn">Learn More</div>
</section>

<section class="news">
  <div class="news-kicker">Birchwell Holdings</div>
  <h2 class="news-title">News Feed</h2>
  <div class="news-list">
    <article class="news-item">
      <div class="news-thumb" role="img" aria-label="Lit modern house at dusk" style="background:linear-gradient(180deg,#1b2a4a 0%,#3b3f55 45%,#c79a5c 70%,#6b5a44 100%)"></div>
      <div class="news-body"><h3>Neque porro quisquam est qui dolorem ipsum quia dolor</h3>
        <p>Lorem ipsum dolor sit amet, consectetur adipiscing elit, sed do eiusmod tempor incididunt ut labore et dolore magna aliqua. Ut enim ad minim veniam, quis nostrud exercitation ullamco laboris nisi</p>
        <time>October 19, 2017 &nbsp; 8:45PM</time></div>
    </article>
    <article class="news-item">
      <div class="news-thumb" role="img" aria-label="Two-storey family home under blue sky" style="background:linear-gradient(180deg,#1f5fc4 0%,#3f7ad0 40%,#d9dde2 60%,#8a8f94 100%)"></div>
      <div class="news-body"><h3>Neque porro quisquam est qui dolorem ipsum quia dolor</h3>
        <p>Lorem ipsum dolor sit amet, consectetur adipiscing elit, sed do eiusmod tempor incididunt ut labore et dolore magna aliqua. Ut enim ad minim veniam, quis nostrud exercitation ullamco laboris nisi</p>
        <time>October 19, 2017 &nbsp; 8:45PM</time></div>
    </article>
    <article class="news-item">
      <div class="news-thumb" role="img" aria-label="House keys being handed over in an empty room" style="background:linear-gradient(135deg,#c9bba4 0%,#e4dccd 50%,#a89478 100%)"></div>
      <div class="news-body"><h3>Neque porro quisquam est qui dolorem ipsum quia dolor</h3>
        <p>Lorem ipsum dolor sit amet, consectetur adipiscing elit, sed do eiusmod tempor incididunt ut labore et dolore magna aliqua. Ut enim ad minim veniam, quis nostrud exercitation ullamco laboris nisi</p>
        <time>October 19, 2017 &nbsp; 8:45PM</time></div>
    </article>
    <article class="news-item">
      <div class="news-thumb" role="img" aria-label="Stone house with garden and driveway" style="background:linear-gradient(180deg,#3c86d8 0%,#7aa6c8 35%,#9c8a6e 60%,#4f7a32 100%)"></div>
      <div class="news-body"><h3>Neque porro quisquam est qui dolorem ipsum quia dolor</h3>
        <p>Lorem ipsum dolor sit amet, consectetur adipiscing elit, sed do eiusmod tempor incididunt ut labore et dolore magna aliqua. Ut enim ad minim veniam, quis nostrud exercitation ullamco laboris nisi</p>
        <time>October 19, 2017 &nbsp; 8:45PM</time></div>
    </article>
    <article class="news-item">
      <div class="news-thumb" role="img" aria-label="City skyline at sunset" style="background:linear-gradient(180deg,#6f9cc4 0%,#d9b57a 50%,#6a6a5e 100%)"></div>
      <div class="news-body"><h3>Neque porro quisquam est qui dolorem ipsum quia dolor</h3>
        <p>Lorem ipsum dolor sit amet, consectetur adipiscing elit, sed do eiusmod tempor incididunt ut labore et dolore magna aliqua. Ut enim ad minim veniam, quis nostrud exercitation ullamco laboris nisi</p>
        <time>October 19, 2017 &nbsp; 8:45PM</time></div>
    </article>
  </div>
  <div class="scroll-track"><div class="scroll-thumb"></div></div>
</section>

<footer class="site-footer">
  <div class="foot-nav">Home &nbsp;|&nbsp; Birchwell Team &nbsp;|&nbsp; Services &nbsp;|&nbsp; Sold Properties &nbsp;|&nbsp; Contact</div>
  <div class="foot-brand">Birchwell</div>
  <div class="copyright">© 2017 Company Name &nbsp;|&nbsp; All Rights Reserved</div>
</footer>

</body>
</html>
```